Voxnook

We need a 1 page flyer to showcase our public access phonebooth.
Hearthside Wellness Outreach Office
Connecting ones in need with loved ones
Flyer to indicate wired or wireless options.
The phone is VOIP based
LED lighting
Wireless option includes solar generation, and battery supply
Pictures need to be touched up to show warm summertime atmosphere
Quillmoor Color Pallette to be followed
www.quillmoorrenewables.example
email sales@quillmoorrenewables.example
Phone 780.555.0163

```html
<!DOCTYPE html>
<html lang="en">
<head>
<meta charset="utf-8">
<title>Voxnook Public Access Phonebooth Flyer</title>
<link rel="stylesheet" href="https://fonts.googleapis.com/css2?family=Poppins:wght@400;500;600;700&family=Oswald:wght@600&display=swap">
<style>
  :root {
    --navy: #2f3b8f;
    --booth-blue: #2a47a6;
    --green: #6bbd3e;
    --green-dark: #4f9a2a;
    --sky: #3fbde8;
    --yellow: #f4e01c;
    --steel: #b8bdc3;
    --ink: #2b2b33;
    --paper: #ffffff;
    --backdrop: #dcdcdc;
  }
  * { margin: 0; padding: 0; box-sizing: border-box; }
  html, body { width: 763px; height: 1200px; overflow: hidden; background: var(--backdrop); }
  .canvas { position: relative; width: 763px; height: 1200px; }
  .flyer {
    position: absolute; left: 0; top: 61px;
    width: 800px; height: 1130px;
    transform: scale(0.95375); transform-origin: top left;
    background: var(--paper); overflow: hidden;
    font-family: "Poppins", sans-serif; color: var(--ink);
  }
  .flyer-art { position: absolute; inset: 0; }
  .brand {
    position: absolute; left: 58px; top: 112px;
    display: flex; align-items: center; gap: 10px;
    font-weight: 700; font-size: 30px; color: var(--navy); letter-spacing: 0.5px;
  }
  .brand-dot { width: 16px; height: 16px; border-radius: 50%; background: var(--sky); }
  .eyebrow {
    position: absolute; left: 54px; top: 268px;
    color: #fff; font-weight: 500; font-size: 29px; letter-spacing: 8px;
  }
  .headline-bar {
    position: absolute; left: 54px; top: 310px; width: 345px; height: 88px;
    background: var(--navy); border-radius: 8px 0 0 8px;
    box-shadow: 0 4px 8px rgba(0,0,0,.25);
  }
  .headline {
    position: absolute; left: 18px; top: 4px;
    font-family: "Oswald", sans-serif; font-weight: 600; font-size: 60px; line-height: 80px;
    color: #fff; letter-spacing: 0.5px;
  }
  .partner {
    position: absolute; left: 55px; top: 438px; padding-left: 22px;
    border-left: 7px solid var(--yellow);
    color: #fff; font-weight: 600; font-size: 26px; line-height: 32px; width: 330px;
  }
  .booth-sign {
    position: absolute; color: #fff; font-weight: 600; letter-spacing: 0.5px;
    display: flex; align-items: center; gap: 6px;
  }
  .booth-sign .sign-dot { width: 10px; height: 10px; border-radius: 50%; border: 2px solid #fff; }
  .booth-sign--hero { left: 555px; top: 88px; font-size: 16px; transform: rotate(3deg); }
  .booth-sign--interior { left: 96px; top: 790px; font-size: 19px; }
  .wireless { position: absolute; left: 55px; top: 658px; }
  .wireless-title { color: var(--sky); font-weight: 700; font-size: 22.5px; letter-spacing: 0.2px; }
  .wireless-items { display: flex; align-items: center; margin-top: 6px; }
  .wireless-item { display: flex; align-items: center; gap: 10px; font-weight: 500; font-size: 18px; line-height: 22px; }
  .wireless-divider { width: 1px; height: 46px; background: #d0d0d0; margin: 0 24px 0 28px; }
  .features { position: absolute; left: 460px; top: 612px; width: 290px; }
  .feature {
    display: flex; align-items: center; gap: 20px; height: 86px;
    border-bottom: 2px dotted var(--sky);
    font-weight: 500; font-size: 19px; line-height: 23px;
  }
  .feature:last-child { border-bottom: none; }
  .feature-icon {
    flex: 0 0 74px; height: 74px; border-radius: 50%;
    border: 3px solid var(--green); padding: 3px; background: #fff;
  }
  .feature-icon svg { display: block; width: 62px; height: 62px; }
  .tagline {
    position: absolute; left: 462px; top: 880px;
    font-weight: 700; font-size: 28px; line-height: 30px;
  }
  .tagline .t1 { color: var(--sky); }
  .tagline .t2 { color: var(--navy); }
  .tagline .t3 { color: var(--green); }
  .tagline-rule { position: absolute; left: 462px; top: 978px; width: 58px; height: 2px; background: #b5b5b5; }
  .contact { position: absolute; left: 462px; top: 990px; font-weight: 500; font-size: 16px; line-height: 24px; }
  .contact-line { display: flex; align-items: center; gap: 6px; }
  .url-pill {
    position: absolute; left: 400px; top: 1050px; width: 352px; height: 48px;
    background: var(--navy); border-radius: 8px;
    box-shadow: 0 5px 8px rgba(0,0,0,.3);
    color: #fff; font-weight: 500; font-size: 17px; letter-spacing: 0.8px;
    display: flex; align-items: center; justify-content: center;
  }
</style>
</head>
<body>
<div class="canvas">
  <div class="flyer">
    <svg class="flyer-art" viewBox="0 0 800 1130" width="800" height="1130">
      <defs>
        <linearGradient id="heroGreen" x1="0" y1="0" x2="0" y2="1">
          <stop offset="0" stop-color="#86c955"/>
          <stop offset="0.5" stop-color="#5fae34"/>
          <stop offset="1" stop-color="#72c243"/>
        </linearGradient>
        <linearGradient id="boothPhoto" x1="0" y1="0" x2="0" y2="1">
          <stop offset="0" stop-color="#d4d7da"/>
          <stop offset="0.14" stop-color="#9aa6b8"/>
          <stop offset="0.2" stop-color="#2c4aa6"/>
          <stop offset="0.68" stop-color="#2744a0"/>
          <stop offset="0.8" stop-color="#4f8f37"/>
          <stop offset="1" stop-color="#6cbf3f"/>
        </linearGradient>
        <linearGradient id="boothEdge" x1="0" y1="0" x2="1" y2="0">
          <stop offset="0" stop-color="#6aae48"/>
          <stop offset="0.12" stop-color="#7d8a94"/>
          <stop offset="0.2" stop-color="#7d8a94" stop-opacity="0"/>
          <stop offset="0.85" stop-color="#5c7b3c" stop-opacity="0"/>
          <stop offset="1" stop-color="#5c7b3c"/>
        </linearGradient>
        <linearGradient id="interiorPhoto" x1="0" y1="0" x2="1" y2="0">
          <stop offset="0" stop-color="#2d4fb3"/>
          <stop offset="0.2" stop-color="#8e98a6"/>
          <stop offset="0.5" stop-color="#c4c9ce"/>
          <stop offset="0.8" stop-color="#8e98a6"/>
          <stop offset="1" stop-color="#2d4fb3"/>
        </linearGradient>
        <linearGradient id="interiorRoof" x1="0" y1="0" x2="0" y2="1">
          <stop offset="0" stop-color="#2b4aa8"/>
          <stop offset="1" stop-color="#2b4aa8" stop-opacity="0"/>
        </linearGradient>
        <linearGradient id="insetPhoto" x1="0" y1="0" x2="0" y2="1">
          <stop offset="0" stop-color="#dfe3e6"/>
          <stop offset="0.2" stop-color="#2b47a3"/>
          <stop offset="0.75" stop-color="#2b47a3"/>
          <stop offset="1" stop-color="#62b23a"/>
        </linearGradient>
      </defs>

      <!-- hero green band -->
      <path d="M0,165 C120,125 260,195 400,150 L800,120 L800,620 C660,555 520,560 400,600 C260,645 110,630 0,590 Z" fill="url(#heroGreen)"/>

      <!-- booth photograph -->
      <g role="img" aria-label="Photo of the blue Voxnook public access phone booth with steel frame in a sunny summer park">
        <path d="M395,0 L800,0 L800,600 C690,565 560,560 420,598 L395,598 Z" fill="url(#boothPhoto)"/>
        <path d="M395,0 L800,0 L800,600 C690,565 560,560 420,598 L395,598 Z" fill="url(#boothEdge)"/>
      </g>
      <!-- booth roof sign band -->
      <path d="M520,78 L720,88 L730,112 L510,100 Z" fill="var(--navy)"/>

      <!-- lower white sweep and green edge -->
      <path d="M0,595 C130,640 280,640 420,605 C570,565 700,560 800,630 L800,1130 L0,1130 Z" fill="#fff"/>
      <path d="M410,607 C560,568 700,565 800,630" fill="none" stroke="var(--green)" stroke-width="7"/>

      <!-- wireless arcs -->
      <g fill="none" stroke="var(--sky)" stroke-linecap="round" stroke-width="24">
        <path d="M308,122 A140,140 0 0 1 464,32"/>
        <path d="M355,139 A90,90 0 0 1 456,81"/>
        <path d="M402,156 A40,40 0 0 1 447,131"/>
      </g>

      <!-- interior photograph -->
      <path d="M0,782 C130,745 270,750 410,800" fill="none" stroke="var(--green)" stroke-width="8"/>
      <g role="img" aria-label="Photo of the Voxnook booth interior with steel walls and a wall mounted VOIP handset">
        <path d="M0,790 C130,754 270,758 400,805 L400,1130 L0,1130 Z" fill="url(#interiorPhoto)"/>
        <path d="M0,790 C130,754 270,758 400,805 L400,900 L0,900 Z" fill="url(#interiorRoof)"/>
      </g>
      <circle cx="340" cy="875" r="90" fill="var(--green)"/>
      <g role="img" aria-label="Photo of the complete Voxnook booth seen from the front">
        <circle cx="340" cy="875" r="76" fill="url(#insetPhoto)"/>
      </g>
    </svg>

    <div class="booth-sign booth-sign--hero"><span class="sign-dot"></span>Voxnook</div>
    <div class="booth-sign booth-sign--interior"><span class="sign-dot"></span>Voxnook</div>

    <div class="brand"><span class="brand-dot"></span>Quillmoor</div>

    <div class="eyebrow">PUBLIC ACCESS</div>
    <div class="headline-bar"><div class="headline">PHONEBOOTH</div></div>
    <div class="partner">Hearthside Wellness Outreach Office</div>

    <div class="wireless">
      <div class="wireless-title">WIRELESS OPTION INCLUDES</div>
      <div class="wireless-items">
        <div class="wireless-item">
          <svg width="34" height="36" viewBox="0 0 34 36" aria-hidden="true">
            <circle cx="17" cy="8" r="4.5" fill="var(--navy)"/>
            <g stroke="var(--navy)" stroke-width="2" stroke-linecap="round">
              <line x1="17" y1="0.5" x2="17" y2="1.5"/><line x1="9" y1="8" x2="10.5" y2="8"/><line x1="23.5" y1="8" x2="25" y2="8"/>
              <line x1="11.5" y1="2.5" x2="12.5" y2="3.5"/><line x1="22.5" y1="2.5" x2="21.5" y2="3.5"/>
            </g>
            <path d="M6,17 H28 L32,35 H2 Z" fill="var(--navy)"/>
            <g stroke="#fff" stroke-width="1.4"><line x1="4" y1="23" x2="30" y2="23"/><line x1="3" y1="29" x2="31" y2="29"/><line x1="13" y1="17" x2="12" y2="35"/><line x1="21" y1="17" x2="22" y2="35"/></g>
          </svg>
          <span>Solar<br>generation</span>
        </div>
        <div class="wireless-divider"></div>
        <div class="wireless-item">
          <svg width="24" height="40" viewBox="0 0 24 40" aria-hidden="true">
            <rect x="8" y="0" width="8" height="4" rx="1" fill="var(--navy)"/>
            <rect x="2" y="4" width="20" height="35" rx="3" fill="none" stroke="var(--navy)" stroke-width="2.5"/>
            <rect x="6" y="12" width="12" height="23" rx="1" fill="var(--navy)"/>
          </svg>
          <span>Battery<br>supply</span>
        </div>
      </div>
    </div>

    <div class="features">
      <div class="feature">
        <div class="feature-icon">
          <svg viewBox="0 0 62 62" aria-hidden="true">
            <circle cx="31" cy="31" r="31" fill="var(--navy)"/>
            <g fill="none" stroke="#fff" stroke-width="3.5" stroke-linecap="round">
              <path d="M17,27 A20,20 0 0 1 45,27"/><path d="M22,33 A13,13 0 0 1 40,33"/>
            </g>
            <circle cx="31" cy="39" r="3" fill="#fff"/>
          </svg>
        </div>
        <span>Wired or wireless<br>options</span>
      </div>
      <div class="feature">
        <div class="feature-icon">
          <svg viewBox="0 0 62 62" aria-hidden="true">
            <circle cx="31" cy="31" r="31" fill="var(--navy)"/>
            <circle cx="33" cy="31" r="14" fill="#fff"/>
            <path d="M22,20 l5,-2 3,7 -3,2 c1,4 4,7 8,8 l2,-3 7,3 -2,5 c-11,0 -20,-9 -20,-20 z" fill="var(--navy)" stroke="#fff" stroke-width="2"/>
          </svg>
        </div>
        <span>The phone<br>is VOIP based</span>
      </div>
      <div class="feature">
        <div class="feature-icon">
          <svg viewBox="0 0 62 62" aria-hidden="true">
            <circle cx="31" cy="31" r="31" fill="var(--navy)"/>
            <path d="M23,42 V32 A8,8 0 0 1 39,32 V42 Z" fill="#fff"/>
            <rect x="19" y="42" width="24" height="4" rx="1" fill="#fff"/>
            <g stroke="#fff" stroke-width="2.5" stroke-linecap="round">
              <line x1="31" y1="14" x2="31" y2="18"/><line x1="18" y1="20" x2="21" y2="23"/><line x1="44" y1="20" x2="41" y2="23"/>
              <line x1="14" y1="31" x2="17" y2="31"/><line x1="45" y1="31" x2="48" y2="31"/>
            </g>
          </svg>
        </div>
        <span>LED lighting</span>
      </div>
    </div>

    <div class="tagline">
      <div class="t1">CONNECTING</div>
      <div class="t2">ONES IN NEED WITH</div>
      <div class="t3">LOVED ONES</div>
    </div>
    <div class="tagline-rule"></div>

    <div class="contact">
      <div class="contact-line">
        <svg width="13" height="10" viewBox="0 0 13 10" aria-hidden="true"><rect width="13" height="10" rx="1" fill="var(--sky)"/><path d="M0.5,1 L6.5,6 L12.5,1" fill="none" stroke="#fff" stroke-width="1.3"/></svg>
        <span>sales@quillmoorrenewables.example</span>
      </div>
      <div class="contact-line">
        <svg width="13" height="13" viewBox="0 0 13 13" aria-hidden="true"><path d="M2,1 l3,0 1,3 -2,1.5 c1,2 2,3 4,4 l1.5,-2 3,1 0,3 c-6,0 -10.5,-4.5 -10.5,-10.5 z" fill="var(--sky)"/></svg>
        <span>780.555.0163</span>
      </div>
    </div>

    <div class="url-pill">www.quillmoorrenewables.example</div>
  </div>
</div>
</body>
</html>
```